Business card design needed

I run a Beautician studio (for 7 years now)
I offer
- Vestolin Body Sugaring
- Velumi Glow
- Nails
- Facials
- Manicure
- Foot Treatment
It might not be necessary to list all those treatments?
Maybe the link to the Website is sufficient?
I leave that up to you ...
(more info on www.BuffsAndBrowsByMarisol.com.au)
Vestolin BodySugaring is our biggest success, It replaces waxing.
I would like to incorporate the logo into the Business Card.
We had many complaints regarding our old Business Cards as the Phone Number was to small.
On the backside, we would like a "your next Appointment" section.
Looking forward to you Design, cheers ... Marisol
Buffs by Brows by Marisol
14 Merindo Cct 3912 Berwick
www.BuffsAndBrowsByMarisol.com.au
03 9418 2276

```html
<!DOCTYPE html>
<html lang="en">
<head>
<meta charset="utf-8">
<title>Buffs&amp;Brows by Marisol – Business Card</title>
<link rel="stylesheet" href="https://fonts.googleapis.com/css2?family=Tinos:wght@400;700&display=swap">
<style>
  :root {
    --backdrop: #ece6de;
    --card-white: #ffffff;
    --pale-yellow: #fbf6c4;
    --sun-yellow: #f6e83a;
    --amber: #f4a92c;
    --orange: #f07a28;
    --red-orange: #e9452a;
    --ink: #111111;
    --logo-mark: #f29a2e;
    --logo-ink: #2b2b2b;
  }
  * { margin: 0; padding: 0; box-sizing: border-box; }
  html, body { width: 1200px; height: 1000px; overflow: hidden; }
  body {
    background: var(--backdrop);
    font-family: "Tinos", "Times New Roman", serif;
    color: var(--ink);
  }
  .canvas {
    position: relative;
    width: 1200px;
    height: 1000px;
  }
  .card {
    position: absolute;
    top: 232px;
    width: 303px;
    height: 537px;
    border-radius: 10px;
    box-shadow: 0 4px 12px rgba(0,0,0,0.22);
    overflow: hidden;
  }
  .card--front {
    left: 184px;
    background: linear-gradient(to bottom,
      var(--card-white) 0%,
      var(--card-white) 38%,
      var(--pale-yellow) 52%,
      var(--sun-yellow) 68%,
      var(--amber) 82%,
      var(--orange) 92%,
      var(--red-orange) 100%);
    text-align: center;
  }
  .card--back {
    left: 755px;
    background: linear-gradient(to bottom,
      var(--red-orange) 0%,
      var(--orange) 9%,
      var(--amber) 18%,
      var(--sun-yellow) 30%,
      var(--pale-yellow) 40%,
      var(--card-white) 48%,
      var(--card-white) 100%);
  }
  .brand-mark {
    position: absolute;
    top: 40px;
    left: 0;
    right: 0;
    display: flex;
    flex-direction: column;
    align-items: center;
  }
  .brand-mark__dot {
    width: 86px;
    height: 86px;
    border-radius: 50%;
    background: var(--logo-mark);
  }
  .brand-mark__name {
    margin-top: 14px;
    font-size: 19px;
    font-weight: 400;
    letter-spacing: 3px;
    color: var(--logo-ink);
    line-height: 1.2;
    text-transform: uppercase;
  }
  .studio-name {
    position: absolute;
    top: 218px;
    left: 0;
    right: 0;
    font-weight: 700;
    line-height: 1.25;
  }
  .studio-name__line { display: block; font-size: 21px; letter-spacing: 2.5px; }
  .studio-name__owner { display: block; font-size: 27px; letter-spacing: 1px; margin-top: 2px; }
  .contact {
    position: absolute;
    top: 370px;
    left: 0;
    right: 0;
    font-weight: 700;
  }
  .contact__address { font-size: 15px; }
  .contact__web { font-size: 13.5px; margin-top: 22px; }
  .contact__phone { font-size: 20px; margin-top: 22px; letter-spacing: 0.5px; }
  .appointment__title {
    position: absolute;
    top: 108px;
    left: 0;
    right: 0;
    text-align: center;
    font-size: 21px;
  }
  .appointment__field {
    position: absolute;
    left: 33px;
    display: flex;
    align-items: flex-end;
    font-size: 21px;
  }
  .appointment__field--date { top: 348px; }
  .appointment__field--time { top: 410px; }
  .appointment__label { width: 70px; }
  .appointment__line {
    width: 170px;
    border-bottom: 2px solid var(--ink);
    margin-bottom: 4px;
  }
</style>
</head>
<body>
<main class="canvas">
  <section class="card card--front" aria-label="Business card front">
    <div class="brand-mark">
      <span class="brand-mark__dot"></span>
      <span class="brand-mark__name">Vestolin Body Sugaring</span>
    </div>
    <h1 class="studio-name">
      <span class="studio-name__line">BUFFS&amp;BROWS</span>
      <span class="studio-name__line">BY</span>
      <span class="studio-name__owner">MARISOL</span>
    </h1>
    <div class="contact">
      <p class="contact__address">14 Merindo Cct 3912 Berwick</p>
      <p class="contact__web">www.BuffsAndBrowsByMarisol.com.au</p>
      <p class="contact__phone">03 9418 2276</p>
    </div>
  </section>

  <section class="card card--back" aria-label="Business card back">
    <p class="appointment__title">your next appointment:</p>
    <div class="appointment__field appointment__field--date">
      <span class="appointment__label">Date:</span>
      <span class="appointment__line"></span>
    </div>
    <div class="appointment__field appointment__field--time">
      <span class="appointment__label">Time:</span>
      <span class="appointment__line"></span>
    </div>
  </section>
</main>
</body>
</html>
```